PLQ Biz Cards and Web Page Design

Hello we are a credit card processing company, a lending company, and payroll company. Seeing how this is a card. I would like to see some clever designs... You could make it look like a credit card, with raised lettering and signature spot on the back. Be creative.
Also this is for a webpage. Our website is www.velderpaytrust.com
Please let me know what you need.

Target Market(s)

Business Owners in the USA.

Industry/Entity Type

Credit Card

Contact Information for Business Card

I've attached our current logo and business cards. I would like you to use the Red, White, and Blue Colors and also maybe try designs that look like credit cards with Raised Text, signature spot in the back and mag strips.

Number of Pages Required

1 page

```html
<!DOCTYPE html>
<html lang="en">
<head>
<meta charset="utf-8">
<title>PLQ Business Card</title>
<link href="https://fonts.googleapis.com/css2?family=Montserrat:wght@500;600;700&family=Roboto:wght@400&display=swap" rel="stylesheet">
<style>
  :root {
    --bg: #e9e9ec;
    --brand-blue: #2d3f98;
    --brand-blue-dark: #24348a;
    --brand-red: #e5262f;
    --ink: #4a4a4a;
    --paper: #ffffff;
  }
  * { margin: 0; padding: 0; box-sizing: border-box; }
  html, body { width: 1200px; height: 900px; overflow: hidden; background: var(--bg); }
  .canvas { position: relative; width: 1200px; height: 900px; }

  .card {
    position: absolute; left: 250px; width: 700px; height: 400px;
    box-shadow: 0 6px 18px rgba(0,0,0,0.18);
  }

  /* Front */
  .card-front { top: 35px; background: linear-gradient(135deg, var(--brand-blue-dark), #3446a6); }
  .world-map {
    position: absolute; left: 120px; top: 60px; width: 470px; height: 280px;
    border-radius: 40px; background: radial-gradient(ellipse at center, rgba(80,100,190,0.45), rgba(80,100,190,0) 70%);
  }
  .front-lockup {
    position: absolute; left: 0; right: 0; top: 135px;
    display: flex; align-items: center; justify-content: center; gap: 26px;
    color: var(--paper); font-family: "Montserrat", sans-serif;
  }
  .front-mark { font-size: 56px; font-weight: 700; letter-spacing: 2px; }
  .front-divider { width: 2px; height: 110px; background: var(--paper); }
  .front-name { display: flex; flex-direction: column; }
  .front-name-main { font-size: 44px; font-weight: 600; letter-spacing: 1px; line-height: 1; }
  .front-name-sub { font-size: 15px; font-weight: 500; letter-spacing: 5px; margin-top: 6px; }

  /* Back */
  .card-back { top: 465px; background: var(--paper); }
  .back-mark {
    position: absolute; left: 80px; top: 140px;
    font-family: "Montserrat", sans-serif; font-size: 100px; font-weight: 700;
    color: var(--brand-red); letter-spacing: 2px; line-height: 1;
  }
  .back-divider { position: absolute; left: 370px; top: 95px; width: 3px; height: 210px; background: var(--brand-blue); }
  .contact { position: absolute; left: 400px; top: 92px; }
  .person-name {
    font-family: "Montserrat", sans-serif; font-weight: 700; font-size: 22px;
    color: var(--brand-blue); letter-spacing: 0.5px;
  }
  .person-title {
    font-family: "Roboto", sans-serif; font-size: 16px; color: var(--ink);
    letter-spacing: 0.5px; margin-bottom: 14px;
  }
  .contact-list { list-style: none; font-family: "Roboto", sans-serif; font-size: 17px; color: var(--ink); }
  .contact-list li { display: flex; align-items: center; gap: 14px; height: 27px; }
  .contact-list svg { width: 14px; height: 14px; fill: var(--brand-red); flex: none; }
</style>
</head>
<body>
<div class="canvas">

  <section class="card card-front">
    <div class="world-map" role="img" aria-label="Dotted world map in a deeper blue"></div>
    <div class="front-lockup">
      <span class="front-mark">PLQ</span>
      <span class="front-divider"></span>
      <div class="front-name">
        <span class="front-name-main">VELDER</span>
        <span class="front-name-sub">PAY TRUST</span>
      </div>
    </div>
  </section>

  <section class="card card-back">
    <div class="back-mark">PLQ</div>
    <div class="back-divider"></div>
    <div class="contact">
      <div class="person-name">DANA R. HOLLOWAY</div>
      <div class="person-title">DIRECTOR OF OPERATIONS</div>
      <ul class="contact-list">
        <li><svg viewBox="0 0 16 16"><path d="M3 1l3 3-2 2c1 2 4 5 6 6l2-2 3 3-2 2C7 15 1 9 1 3z"/></svg>888-555-0147</li>
        <li><svg viewBox="0 0 16 16"><path d="M4 0h8a1 1 0 011 1v14a1 1 0 01-1 1H4a1 1 0 01-1-1V1a1 1 0 011-1zm1 2v10h6V2z"/></svg>860-555-0192</li>
        <li><svg viewBox="0 0 16 16"><path d="M4 1h8v4H4zM1 6h14v6h-3v3H4v-3H1zm4 4v3h6v-3z"/></svg>877-555-0163</li>
        <li><svg viewBox="0 0 16 16"><path d="M0 3h16v2L8 10 0 5zm0 4l8 5 8-5v6H0z"/></svg>danaholloway@mailbox.com</li>
        <li><svg viewBox="0 0 16 16"><path d="M6.5 1a5.5 5.5 0 014.4 8.8l4.4 4.4-1.4 1.4-4.4-4.4A5.5 5.5 0 116.5 1zm0 2a3.5 3.5 0 100 7 3.5 3.5 0 000-7z"/></svg>velderpaytrust.com</li>
      </ul>
    </div>
  </section>

</div>
</body>
</html>
```